Rock Star Designer Needed

I'm looking for a similar wordpress design to the examples below...

I really like the simple, clean design of these example
- http://quillharborguild.net
- http://hub.brightmarrowtips.net

What I like are the simple design ad for webinar at top/bottom and spot for content in the middle.

I specifically like the font on the graphical looking banners from the 2nd site (http://hub.brightmarrowtips.net)

This will be the home of our NEW site at http://www.PebbleLanternSeminarVault.net

Looking for a fun youthful look, inspired by sales letters found at tally grove.

Are you up to the challenge?

Target Market(s)

Internet Marketers, People Looking To Make Money Online

Requirements
Must have
• Real easy to see template style by viewing...
http://quillharborguild.net/

Main Section (Left under header)
- Graphic Section (could be said to be ads) at Top & Bottom of blog - Content Section (text) In the middle (graphic section)
Sidebar (Right side of blog)
- Optin on Top Left of blog sidebar
- Graphic (could be said to be ad) underneath optin
- Categories section under graphic

```html
<!DOCTYPE html>
<html lang="en">
<head>
<meta charset="utf-8">
<title>Pebble Lantern Seminar Vault</title>
<link href="https://fonts.googleapis.com/css2?family=Oswald:wght@500&family=Open+Sans:wght@300;400;600;700&display=swap" rel="stylesheet">
<style>
:root{
  --bg-top:#8e8e8e;
  --bg-bottom:#d6d6d6;
  --page:#ffffff;
  --ad:#c9c9c9;
  --nav-dark:#2f2f2f;
  --nav-tab:#5a5a5a;
  --green:#7ab51d;
  --green-light:#92c81f;
  --green-dark:#5a940c;
  --blue:#1d79b8;
  --text:#333333;
  --muted:#7a7a7a;
  --olive:#4f6a00;
  --panel:#6b6b6b;
  --line:#dcdcdc;
  --red:#e0281e;
}
*{box-sizing:border-box;margin:0;padding:0}
html,body{width:904px;height:1200px;overflow:hidden}
body{background:linear-gradient(var(--bg-top),var(--bg-bottom) 60%);font-family:"Open Sans",Arial,sans-serif;position:relative;color:var(--text)}
.abs{position:absolute}
.page{left:57px;top:33px;width:799px;height:1119px;background:var(--page)}
.brand{left:68px;top:44px;display:flex;align-items:center;gap:10px}
.brand-mark{width:26px;height:26px;border-radius:50%;background:var(--blue)}
.brand-name{font-family:"Open Sans",Arial,sans-serif;font-weight:700;font-size:17px;color:var(--blue);line-height:1.2;width:300px}
.brand-tag{left:68px;top:96px;font-size:12px;font-weight:700;color:var(--blue)}
.ad{background:var(--ad);color:#fff;font-size:12px;display:flex;align-items:center;justify-content:center}
.search{left:697px;top:102px;width:148px;height:21px;border:1px solid #bdbdbd;border-radius:2px;background:#fff}
.search svg{position:absolute;left:5px;top:4px}
.nav{left:57px;top:139px;width:799px;height:36px;background:linear-gradient(#4a4a4a,var(--nav-dark))}
.tab{position:absolute;top:4px;height:32px;width:122px;background:linear-gradient(#707070,var(--nav-tab));color:#fff;font-size:12.5px;text-align:center;line-height:30px;border-radius:3px 3px 0 0}
.tab.active{background:linear-gradient(var(--green-light),var(--green));height:42px;z-index:2}
.hero{left:57px;top:175px;width:799px;height:258px;background:linear-gradient(90deg,#93c41c,#7bb515 55%,#5f9a10)}
.hero-photo{position:absolute;right:0;top:0;width:363px;height:258px;background:linear-gradient(135deg,#2a2a2a,#141414 60%,#3a3a3a)}
.hero-title{left:78px;top:230px;font-family:"Oswald",Arial Narrow,sans-serif;font-weight:500;font-size:25px;line-height:32px;color:#fff;text-shadow:0 1px 2px rgba(0,0,0,.3)}
.hero-sub{left:78px;top:319px;font-size:15px;font-weight:700;line-height:19px;color:#fff}
.btn-light{left:78px;top:367px;width:91px;height:23px;background:linear-gradient(#fff,#d9d9d9);border-radius:3px;box-shadow:0 1px 2px rgba(0,0,0,.4);font-size:12px;line-height:23px;text-align:center;color:#333}
.dot{width:11px;height:11px;border-radius:50%;background:#5a8a12;top:410px}
.dot.on{background:#2a2a2a}
.steps{left:57px;top:433px;width:799px;height:132px;background:linear-gradient(#f5f5f5,#e2e2e2)}
.step{position:absolute;top:0;height:132px;width:262px}
.step+.step{border-left:1px solid #cfcfcf}
.step-num{position:absolute;left:13px;top:12px;font-size:24px;font-weight:700;color:#aaa}
.step-title{position:absolute;left:13px;top:52px;font-size:23px;font-weight:300;color:#b3b3b3}
.step-note{position:absolute;left:13px;top:79px;font-size:12px;color:#bdbdbd}
.step.active .step-num,.step.active .step-title{color:var(--green)}
.step.active .step-note{color:#555}
.step-icon{position:absolute;right:24px;top:30px;width:58px;height:68px;border-radius:6px}
.main-title{left:78px;top:576px;width:520px;font-size:19.5px;font-weight:700;line-height:26px;color:var(--blue)}
.main-sub{left:78px;top:660px;font-size:15.5px;font-weight:700;color:var(--text)}
.copy{left:78px;top:693px;width:520px;font-size:12.3px;line-height:15.5px;color:var(--muted)}
.copy p{margin-bottom:14.5px}
.copy p.highlight{color:var(--olive)}
.btn-green{left:523px;top:1020px;width:61px;height:15px;background:linear-gradient(var(--green-light),var(--green-dark));border-radius:2px;color:#fff;font-size:8.5px;line-height:15px;text-align:center}
.rule{left:72px;top:1049px;width:535px;height:1px;background:var(--line)}
.teaser{left:73px;top:1068px;width:535px;font-size:15.5px;line-height:20px;color:#777}
.teaser-big{left:73px;top:1107px;font-size:21px;color:#222}
.optin{left:624px;top:572px;width:225px;height:289px;background:var(--panel);border-radius:4px;color:#fff}
.optin h2{position:absolute;left:13px;top:10px;font-size:20px;font-weight:300}
.alert{position:absolute;left:13px;top:40px;font-size:10.5px;font-weight:700}
.from{position:absolute;left:13px;top:54px;font-size:9px;color:#e2e2e2}
.label{position:absolute;left:8px;font-size:10px;font-weight:700}
.field{position:absolute;background:#eee;border:1px solid #bbb;height:20px}
.seats{position:absolute;right:8px;top:103px;font-size:8px;color:#e6e6e6}
.submit{position:absolute;left:13px;top:250px;width:202px;height:26px;border-radius:4px;background:linear-gradient(var(--green-light),var(--green-dark));font-size:16px;text-align:center;line-height:26px}
.video{left:625px;top:873px;width:220px;height:127px;background:linear-gradient(#fafafa,#e6e6e6);border:1px solid #ccc}
.ad-side{left:625px;top:1008px;width:220px;height:137px}
.footer-copy{left:64px;top:1173px;font-size:8.5px;color:#777}
.footer-links{left:432px;top:1172px;font-size:9.5px;color:#333}
.social{top:1165px;width:23px;height:23px;border-radius:3px}
</style>
</head>
<body>
<div class="abs page"></div>

<div class="abs brand"><span class="brand-mark"></span><span class="brand-name">Pebble Lantern Seminar Vault</span></div>
<div class="abs brand-tag">Your Blueprint To Wealth &amp; Freedom</div>
<div class="abs ad" style="left:418px;top:37px;width:433px;height:58px">Ad</div>
<div class="abs search"><svg width="12" height="12" viewBox="0 0 12 12"><circle cx="5" cy="5" r="3.5" fill="none" stroke="#333" stroke-width="1.6"/><line x1="7.5" y1="7.5" x2="11" y2="11" stroke="#333" stroke-width="1.8"/></svg></div>

<nav class="abs nav">
  <div class="tab active" style="left:21px">Home</div>
  <div class="tab" style="left:151px">About us</div>
  <div class="tab" style="left:280px">Services</div>
  <div class="tab" style="left:411px">Free Webinar</div>
  <div class="tab" style="left:540px">What you get</div>
  <div class="tab" style="left:670px">Contact us</div>
</nav>

<section class="abs hero">
  <div class="hero-photo" role="img" aria-label="Businessman in a dark suit holding out a black gift box tied with a red ribbon"></div>
</section>
<h1 class="abs hero-title">A New, Plug-In-And-Play Webinar<br>System With The Potential To</h1>
<div class="abs hero-sub">Explode Your Biz Cash-Flow<br>Almost Overnight!</div>
<div class="abs btn-light">Read more</div>
<span class="abs dot on" style="left:75px"></span>
<span class="abs dot" style="left:93px"></span>
<span class="abs dot" style="left:113px"></span>
<span class="abs dot" style="left:132px"></span>

<section class="abs steps">
  <div class="step active" style="left:0">
    <div class="step-num">1</div><div class="step-title">Choose Date</div><div class="step-note">Select your date &nbsp;›</div>
    <div class="step-icon" role="img" aria-label="Wall calendar page showing the number 12" style="background:linear-gradient(#e04a3a 30%,#f4f4f4 30%)"></div>
  </div>
  <div class="step" style="left:262px">
    <div class="step-num">2</div><div class="step-title">Choose Time</div><div class="step-note">Select your time &nbsp;›</div>
    <div class="step-icon" role="img" aria-label="Silver alarm clock" style="background:radial-gradient(circle,#f4f4f4 45%,#9a9a9a 47%,#d0d0d0 70%,transparent 72%)"></div>
  </div>
  <div class="step" style="left:534px">
    <div class="step-num">3</div><div class="step-title">Get free bonus</div><div class="step-note">Select your scheme &nbsp;›</div>
    <div class="step-icon" role="img" aria-label="Blue bowling ball and white bowling pin" style="background:radial-gradient(circle at 40% 65%,#3a7ad0 30%,transparent 32%),linear-gradient(90deg,transparent 70%,#f0f0f0 70%)"></div>
  </div>
</section>

<svg class="abs" style="left:590px;top:528px" width="50" height="82" viewBox="0 0 50 82" aria-hidden="true">
  <path d="M30 4 C8 14 2 40 36 74" fill="none" stroke="var(--red)" stroke-width="2.5" stroke-linecap="round"/>
  <path d="M26 70 L37 76 L38 63" fill="none" stroke="var(--red)" stroke-width="2.5" stroke-linecap="round" stroke-linejoin="round"/>
</svg>

<h2 class="abs main-title">A New, Plug-In-And-Play Webinar System With The Potential To Explode Your Biz Cash-Flow Almost Overnight!</h2>
<h3 class="abs main-sub">During This FREE Webinar you'll find out exactly how you can:</h3>
<div class="abs copy">
  <p>Discover a proven 12 step system you can use to build killer webinar presentations for maximum response and high conversions...in any customer base you want to capture and dominate!</p>
  <p>Gain the five simple steps with the power to transform automated webinars into your reliable, cash-pulling bullet train...running day and night.</p>
  <p>Learn how online and offline business owners with NO prior experience are using this amazing system to generate almost "instant" cash-flow in less than 24 hours...</p>
  <p>How to cash in on a HOT gold rush NOW through the top sources for quality buyer traffic...and dozens of ways you can drive them to your webinars!</p>
  <p>Get the full story how two newbie entrepreneurs built multi-millions in wealth with mega-successful webinar campaigns...and how you can do it today!</p>
  <p class="highlight">Let Pebble Lantern Seminar Vault do all the work for you... while you gain new customers like crazy and generate a terrific income!</p>
  <p>Plus tons more...jump on it now, we only have 70 front-row seats available, reserve your seat right now...</p>
</div>
<div class="abs btn-green">Read more</div>
<div class="abs rule"></div>
<div class="abs teaser">NEW Game Changing System That Converts Prospects Into Customers On Autopilot...</div>
<div class="abs teaser-big">Yes, Even While You Sleep!</div>

<aside class="abs optin">
  <h2>Register Free Now</h2>
  <div class="alert">Urgent Alert: Only 70 Seats Available!</div>
  <div class="from">From Marrowville Change the Game &amp; Unleash:</div>
  <div class="label" style="top:82px">Choose a date:</div>
  <div class="field" style="left:88px;top:78px;width:129px">
    <svg style="position:absolute;right:3px;top:3px" width="14" height="12" viewBox="0 0 14 12"><rect x=".5" y=".5" width="13" height="11" fill="#fff" stroke="#4a7ac0"/><rect x=".5" y=".5" width="13" height="3" fill="#4a7ac0"/></svg>
  </div>
  <div class="seats">(Only 300 70 seats left for this event time.)</div>
  <div class="label" style="top:128px">Choose a Time:</div>
  <div class="field" style="left:88px;top:124px;width:35px;font-size:10px;color:#333;padding:3px">00</div>
  <div class="field" style="left:130px;top:124px;width:37px;font-size:10px;color:#333;padding:3px">00</div>
  <div class="field" style="left:174px;top:124px;width:43px;font-size:10px;color:#333;padding:3px">AM ▾</div>
  <div class="label" style="top:165px">Name:</div>
  <div class="field" style="left:88px;top:160px;width:129px"></div>
  <div class="label" style="top:201px">Email:</div>
  <div class="field" style="left:88px;top:197px;width:129px"></div>
  <div class="submit">Submit Registration</div>
</aside>

<div class="abs video" role="img" aria-label="Hand-drawn whiteboard video still with sketched business people and a play button"></div>
<div class="abs ad ad-side">Ad</div>

<div class="abs footer-copy">Copyright © 2009-2011 by Pebble Lantern Seminar Vault. All Rights Reserved.</div>
<div class="abs footer-links">Terms of Use | Disclaimer | Privacy Policy</div>
<span class="abs social" style="left:690px;background:#3b5a9a"></span>
<span class="abs social" style="left:716px;background:#3aa6d8"></span>
<span class="abs social" style="left:742px;background:#e8822a"></span>
<span class="abs social" style="left:768px;background:#6a2a8a"></span>
<span class="abs social" style="left:794px;background:#e87a20"></span>
<span class="abs social" style="left:820px;background:#b92a22"></span>
</body>
</html>
```